Dr Tasneer's Letterhead

I need a professional neat letterhead incorporating my professional information, university titles and qualifications. I have attached my 3 recent ones which contain all the necessary information that needs to be included. I am happy for the information to be a side bar left or right, or as a header/footer combination.

Hello all

I have now made a 2nd and 3rd prize so please submit

Reason: Now there is a 2nd and 3rd place so I can take 3 designs

Industry/Entity Type

University

```html
<!DOCTYPE html>
<html lang="en">
<head>
<meta charset="utf-8">
<title>Dr Tasneer Letterhead</title>
<link href="https://fonts.googleapis.com/css2?family=Arimo:wght@400;700&display=swap" rel="stylesheet">
<style>
  :root {
    --paper: #fdfbf4;
    --navy: #2b3a8f;
    --band-red: #e0262d;
    --band-gold: #d9a35a;
    --footer-blue: #3c4798;
    --white: #ffffff;
    --crest-gold: #e5c873;
    --crest-navy: #2f3f87;
    --college-sage: #dfe6df;
  }
  * { margin: 0; padding: 0; box-sizing: border-box; }
  html, body { width: 927px; height: 1200px; overflow: hidden; background: var(--paper); }
  .letterhead {
    position: relative;
    width: 927px;
    height: 1200px;
    background: var(--paper);
    font-family: "Arimo", Arial, sans-serif;
    overflow: hidden;
  }
  .header-band {
    position: absolute;
    left: 0; top: 0;
    width: 927px; height: 146px;
  }
  .doctor-name {
    position: absolute;
    top: 22px; left: 0; width: 927px;
    text-align: center;
    font-weight: 700;
    font-size: 49px;
    letter-spacing: -0.5px;
    color: var(--navy);
    text-shadow: 0 1px 0 rgba(0,0,0,0.25);
    z-index: 2;
  }
  .credentials {
    position: absolute;
    left: 50px; top: 133px;
    font-size: 16.3px;
    line-height: 21.4px;
    color: var(--navy);
  }
  .affiliations {
    position: absolute;
    top: 132px; left: 514px;
    display: flex;
    gap: 10px;
    align-items: flex-start;
  }
  .affiliation-badge { display: block; }
  .footer {
    position: absolute;
    left: 0; bottom: 0;
    width: 927px; height: 150px;
  }
  .footer-shape { position: absolute; inset: 0; }
  .addresses {
    position: absolute;
    left: 50px; top: 24px;
    width: 440px;
    font-weight: 700;
    font-size: 19.2px;
    line-height: 24.5px;
    color: var(--white);
    text-shadow: 1px 1px 1px rgba(0,0,0,0.45);
  }
  .phone-lines {
    position: absolute;
    left: 526px; top: 26px;
    font-weight: 700;
    font-size: 25px;
    line-height: 32px;
    color: var(--white);
    text-shadow: 1px 1px 1px rgba(0,0,0,0.45);
  }
</style>
</head>
<body>
<div class="letterhead">
  <svg class="header-band" viewBox="0 0 700 110" preserveAspectRatio="none" aria-hidden="true">
    <polygon points="0,79 350,57 700,79 700,84 350,63 0,84" fill="var(--band-gold)"/>
    <polygon points="25,82 350,62 675,82 350,98" fill="var(--band-red)"/>
    <polygon points="60,101 350,80 640,101 640,104 350,86 60,104" fill="var(--band-gold)"/>
  </svg>
  <h1 class="doctor-name">Dr.Rashed Tasneer</h1>

  <div class="credentials">
    BSc Med, MBBS (Hons 1) UNCE<br>
    MSc, FCSS (Oto-HNS)<br>
    Consultant ENT/Head and Neck Surgeon<br>
    Harbourline Regional Cancer Centre<br>
    Brennfield Hospital and Eastvale Coastal Health District<br>
    (ECLHD)<br>
    Senior Lecturer, University of Carrow (UCar) &amp; Eastvale<br>
    Coast (UEC)
  </div>

  <div class="affiliations">
    <svg class="affiliation-badge" width="100" height="100" viewBox="0 0 100 100" role="img" aria-label="University affiliation badge">
      <path d="M10 6 H90 V52 Q90 84 50 96 Q10 84 10 52 Z" fill="var(--crest-gold)"/>
    </svg>
    <svg class="affiliation-badge" width="108" height="100" viewBox="0 0 108 100" role="img" aria-label="Second university affiliation badge">
      <path d="M6 4 H102 V50 Q102 84 54 97 Q6 84 6 50 Z" fill="var(--crest-navy)"/>
    </svg>
    <svg class="affiliation-badge" width="146" height="86" viewBox="0 0 146 86" role="img" aria-label="Surgical college fellowship badge">
      <rect x="0" y="0" width="146" height="86" fill="var(--college-sage)"/>
    </svg>
  </div>

  <footer class="footer">
    <svg class="footer-shape" viewBox="0 0 927 150" preserveAspectRatio="none" aria-hidden="true">
      <path d="M0 6 Q230 -2 463 2 Q700 6 927 0 V150 H0 Z" fill="var(--footer-blue)"/>
    </svg>
    <div class="addresses">
      Suite 208/63 Calloway Road, Brennfield 2190<br>
      14 Marlowe Highway, Ashcombe 2163<br>
      39 Penhall Street, Kestrel Bay 2781
    </div>
    <div class="phone-lines">
      Tel: 95550142 / 95550387<br>
      Fax: 95550619
    </div>
  </footer>
</div>
</body>
</html>
```